Cigar Ring Design

we are working on a project, which is an eCommerce store for cigars, now instead of selling all kind of existing brands this project is based on a TabacoMillDepot concept where an outlet is linked to an actual Cigar factory,
so the cigar lines sold will come out under a TMD (TabacoMillDepot) brand consisting of various labels, (think Barney Cotter, Ochre Crest, Slate Crest etc) I had an idea for the Cigar Rings for this project, where I put TM in an O (circle) of which I made mock ups (see attachement), now I am not a designer, I am sure a real designer can come up with something more stylish and unique.

```html
<!DOCTYPE html>
<html lang="en">
<head>
<meta charset="utf-8">
<title>TabacoMillDepot Cigar Rings</title>
<link rel="stylesheet" href="https://fonts.googleapis.com/css2?family=Oswald:wght@600&display=swap">
<style>
  :root {
    --strip: #000000;
    --stage-light: #dcdcdc;
    --stage-dark: #c4c4c4;
    --gold: #f2b01e;
    --gold-deep: #c8800f;
    --gold-light: #ffd866;
    --seal-face: #f7d37f;
    --ink: #2e2e30;
    --leaf-dark: #6a3a1d;
    --leaf: #9a5e36;
    --leaf-light: #b0744a;
    --band-cream: #e8cb8a;
    --band-green: #33764a;
    --band-black: #0c0c0c;
    --band-silver: #d6d6d6;
    --band-blue: #1e2590;
    --band-red: #d8282c;
  }
  * { box-sizing: border-box; margin: 0; padding: 0; }
  html, body { width: 1200px; height: 1015px; overflow: hidden; }
  body { position: relative; background: var(--strip); font-family: "Oswald", sans-serif; }

  .strip { position: absolute; left: 0; width: 1200px; background: var(--strip); }
  .strip--top { top: 0; height: 168px; }
  .strip--bottom { top: 843px; height: 172px; }
  .stage {
    position: absolute; left: 0; top: 168px; width: 1200px; height: 675px;
    background: radial-gradient(ellipse at 50% 45%, var(--stage-light), var(--stage-dark));
  }

  /* flat ring artwork */
  .ring { position: absolute; width: 240px; height: 120px; }
  .ring--cream  { --band: var(--band-cream);  left: 122px; top: 24px; }
  .ring--green  { --band: var(--band-green);  left: 496px; top: 24px; }
  .ring--black  { --band: var(--band-black);  left: 870px; top: 24px; }
  .ring--silver { --band: var(--band-silver); left: 122px; top: 871px; }
  .ring--blue   { --band: var(--band-blue);   left: 490px; top: 871px; }
  .ring--red    { --band: var(--band-red);    left: 859px; top: 871px; }
  .ring svg { display: block; width: 100%; height: 100%; overflow: visible; }
  .ring__body { fill: var(--band); stroke: var(--gold); stroke-width: 3; }
  .ring__rule { stroke: var(--gold-deep); stroke-width: 1.2; }
  .ring__ornament { fill: var(--gold-deep); opacity: 0.22; }
  .seal__rim { fill: url(#sealRim); }
  .seal__line { fill: none; stroke: #a8620a; stroke-width: 1.2; }
  .seal__face { fill: var(--seal-face); stroke: var(--gold-deep); stroke-width: 1.5; }
  .seal__monogram { fill: var(--ink); font-family: "Oswald", sans-serif; font-weight: 600; font-size: 27px; }
  .ring__badge { fill: var(--gold-light); stroke: var(--gold); stroke-width: 2; }

  /* cigars on the stage */
  .cigar { position: absolute; top: 252px; height: 518px; }
  .cigar__leaf {
    position: absolute; inset: 0;
    border-radius: 48px 48px 42px 42px / 34px 34px 30px 30px;
    background: linear-gradient(90deg, var(--leaf-dark), var(--leaf) 22%, var(--leaf-light) 50%, var(--leaf) 78%, var(--leaf-dark));
  }
  .cigar__band {
    position: absolute; left: -2px; right: -2px; top: 62px; height: 134px;
    background: var(--band);
    border-top: 4px solid var(--gold);
    border-bottom: 4px solid var(--gold);
  }
  .cigar__scroll {
    position: absolute; left: 0; right: 0; top: 50%; height: 34px; margin-top: -17px;
    background: var(--gold-deep); opacity: 0.22;
  }
  .cigar__seal { position: absolute; left: 50%; top: 50%; width: 100px; height: 92px; margin: -46px 0 0 -50px; overflow: visible; }
  .cigar__seal .seal__monogram { font-size: 34px; }
  .cigar--cream  { --band: var(--band-cream);  left: 124px; width: 121px; }
  .cigar--silver { --band: var(--band-silver); left: 297px; width: 110px; }
  .cigar--blue   { --band: var(--band-blue);   left: 475px; width: 103px; }
  .cigar--green  { --band: var(--band-green);  left: 645px; width: 106px; }
  .cigar--black  { --band: var(--band-black);  left: 809px; width: 115px; }
  .cigar--red    { --band: var(--band-red);    left: 983px; width: 127px; }
</style>
</head>
<body>
  <svg width="0" height="0" style="position:absolute" aria-hidden="true">
    <defs>
      <radialGradient id="sealRim" cx="50%" cy="40%" r="60%">
        <stop offset="0" stop-color="#ffd35a"/>
        <stop offset="0.7" stop-color="#e79a1c"/>
        <stop offset="1" stop-color="#b86d0c"/>
      </radialGradient>
      <g id="ringArt">
        <path class="ring__body" d="M1.5 1.5 H216 A22 22 0 0 1 238 23.5 V96.5 A22 22 0 0 1 216 118.5 H1.5 Z"/>
        <rect class="ring__ornament" x="4" y="46" width="222" height="28" role="img" aria-label="Gold scroll ornament running along the band"/>
        <line class="ring__rule" x1="3" y1="44" x2="228" y2="44"/>
        <line class="ring__rule" x1="3" y1="76" x2="228" y2="76"/>
        <circle class="seal__rim" cx="116" cy="60" r="40" role="img" aria-label="Gold key-pattern seal rim"/>
        <circle class="seal__line" cx="116" cy="60" r="37"/>
        <circle class="seal__line" cx="116" cy="60" r="31"/>
        <circle class="seal__face" cx="116" cy="60" r="27"/>
        <text class="seal__monogram" x="116" y="70" text-anchor="middle">TM</text>
        <circle class="ring__badge" cx="223" cy="60" r="17" role="img" aria-label="Round gold badge"/>
      </g>
      <g id="sealArt">
        <ellipse class="seal__rim" cx="50" cy="46" rx="49" ry="45" role="img" aria-label="Gold key-pattern seal rim"/>
        <ellipse class="seal__line" cx="50" cy="46" rx="45" ry="41"/>
        <ellipse class="seal__line" cx="50" cy="46" rx="38" ry="34"/>
        <ellipse class="seal__face" cx="50" cy="46" rx="34" ry="30"/>
        <text class="seal__monogram" x="50" y="58" text-anchor="middle">TM</text>
      </g>
    </defs>
  </svg>

  <div class="strip strip--top"></div>
  <div class="stage"></div>
  <div class="strip strip--bottom"></div>

  <div class="ring ring--cream"><svg viewBox="0 0 240 120"><use href="#ringArt"/></svg></div>
  <div class="ring ring--green"><svg viewBox="0 0 240 120"><use href="#ringArt"/></svg></div>
  <div class="ring ring--black"><svg viewBox="0 0 240 120"><use href="#ringArt"/></svg></div>

  <div class="cigar cigar--cream">
    <div class="cigar__leaf" role="img" aria-label="Natural leaf cigar"></div>
    <div class="cigar__band"><div class="cigar__scroll"></div><svg class="cigar__seal" viewBox="0 0 100 92"><use href="#sealArt"/></svg></div>
  </div>
  <div class="cigar cigar--silver">
    <div class="cigar__leaf" role="img" aria-label="Natural leaf cigar"></div>
    <div class="cigar__band"><div class="cigar__scroll"></div><svg class="cigar__seal" viewBox="0 0 100 92"><use href="#sealArt"/></svg></div>
  </div>
  <div class="cigar cigar--blue">
    <div class="cigar__leaf" role="img" aria-label="Natural leaf cigar"></div>
    <div class="cigar__band"><div class="cigar__scroll"></div><svg class="cigar__seal" viewBox="0 0 100 92"><use href="#sealArt"/></svg></div>
  </div>
  <div class="cigar cigar--green">
    <div class="cigar__leaf" role="img" aria-label="Natural leaf cigar"></div>
    <div class="cigar__band"><div class="cigar__scroll"></div><svg class="cigar__seal" viewBox="0 0 100 92"><use href="#sealArt"/></svg></div>
  </div>
  <div class="cigar cigar--black">
    <div class="cigar__leaf" role="img" aria-label="Natural leaf cigar"></div>
    <div class="cigar__band"><div class="cigar__scroll"></div><svg class="cigar__seal" viewBox="0 0 100 92"><use href="#sealArt"/></svg></div>
  </div>
  <div class="cigar cigar--red">
    <div class="cigar__leaf" role="img" aria-label="Natural leaf cigar"></div>
    <div class="cigar__band"><div class="cigar__scroll"></div><svg class="cigar__seal" viewBox="0 0 100 92"><use href="#sealArt"/></svg></div>
  </div>

  <div class="ring ring--silver"><svg viewBox="0 0 240 120"><use href="#ringArt"/></svg></div>
  <div class="ring ring--blue"><svg viewBox="0 0 240 120"><use href="#ringArt"/></svg></div>
  <div class="ring ring--red"><svg viewBox="0 0 240 120"><use href="#ringArt"/></svg></div>
</body>
</html>
```